Business Card Design Project

I have attached the logo and the colour pallete for the branding for the company.

Creative designs for business cards are needed.

The Company is modern corporate.

Industry/Entity Type

Business

```html
<!DOCTYPE html>
<html lang="en">
<head>
<meta charset="utf-8">
<title>Waypoint business cards</title>
<link rel="stylesheet" href="https://fonts.googleapis.com/css2?family=Open+Sans:wght@400;600;700&display=swap">
<style>
  :root {
    --backdrop: #3b2d27;
    --paper: #f7f7f6;
    --plum: #6b2a6b;
    --plum-dark: #461544;
    --plum-mid: #6e2466;
    --orange: #f7891f;
    --orange-deep: #ee5424;
    --crimson: #d91e3a;
    --wine: #8a1c4a;
    --charcoal: #3a3a3c;
    --ink: #444;
    --white: #ffffff;
  }
  * { margin: 0; padding: 0; box-sizing: border-box; }
  html, body { width: 1200px; height: 913px; overflow: hidden; }
  body {
    background: var(--backdrop);
    font-family: "Open Sans", Arial, sans-serif;
    position: relative;
  }
  .card {
    position: absolute;
    width: 465px;
    height: 265px;
    overflow: hidden;
    box-shadow: 0 4px 10px rgba(0,0,0,.45);
  }
  .brand-name {
    font-family: "Open Sans", Arial, sans-serif;
    font-weight: 700;
    letter-spacing: -1px;
    line-height: 1;
    white-space: nowrap;
  }
  .label {
    position: absolute;
    color: var(--white);
    font-size: 32px;
    font-weight: 400;
  }

  /* front */
  .card-front { left: 91px; top: 146px; background: var(--paper); }
  .card-front .decor-circle {
    position: absolute; left: 280px; top: 10px;
    width: 170px; height: 170px; border-radius: 50%;
    background: #ececea;
  }
  .card-front .brand-name {
    position: absolute; left: 34px; top: 44px;
    font-size: 56px; color: var(--plum);
  }
  .contact-list {
    position: absolute; left: 34px; top: 148px;
    list-style: none; font-size: 12px; color: var(--ink);
  }
  .contact-list li { display: flex; align-items: center; height: 16.5px; }
  .contact-list svg { width: 10px; height: 10px; margin-right: 7px; }
  .address {
    position: absolute; left: 299px; top: 158px;
    font-size: 12px; line-height: 16px; color: var(--ink);
  }
  .name-band {
    position: absolute; left: 15px; top: 214px;
    width: 465px; height: 28px; border-radius: 14px 0 0 14px;
    background: linear-gradient(90deg, var(--orange-deep), var(--orange) 60%);
  }
  .name-band .person {
    position: absolute; left: 22px; top: 3px;
    font-size: 17px; font-weight: 700; color: var(--white);
  }
  .role-pill {
    position: absolute; left: 266px; top: 214px;
    width: 210px; height: 28px; border-radius: 14px 0 0 14px;
    background: linear-gradient(90deg, var(--wine), var(--crimson));
    color: var(--white); font-size: 15px; padding: 3px 0 0 30px;
  }

  /* backs */
  .card-back { display: flex; align-items: center; justify-content: center; }
  .card-back .brand-name {
    font-size: 50px; color: var(--white);
  }
  .back-plum {
    left: 594px; top: 146px;
    background: linear-gradient(90deg, var(--plum-dark), var(--plum-mid) 50%, var(--plum-dark));
  }
  .back-plum .brand-name { margin-top: -40px; }
  .back-plum .stripe {
    position: absolute; left: 0; top: 214px; width: 450px; height: 28px;
    border-radius: 0 14px 14px 0;
    background: linear-gradient(90deg, var(--orange-deep), var(--orange) 70%, var(--orange-deep));
  }
  .back-plum .stripe-accent {
    position: absolute; left: 0; top: 214px; width: 199px; height: 28px;
    border-radius: 0 14px 14px 0;
    background: linear-gradient(90deg, var(--wine), var(--crimson));
  }
  .back-orange {
    left: 89px; top: 445px;
    background: linear-gradient(90deg, var(--orange-deep), var(--orange) 50%, var(--orange-deep));
  }
  .back-charcoal { left: 587px; top: 445px; background: var(--charcoal); }
</style>
</head>
<body>
  <section class="card card-front">
    <div class="decor-circle"></div>
    <div class="brand-name">waypoint</div>
    <ul class="contact-list">
      <li><svg viewBox="0 0 10 10"><circle cx="5" cy="5" r="5" fill="#ee5424"/><path d="M3 2.5l1 1-0.6 0.8a3 3 0 0 0 2.3 2.3l0.8-0.6 1 1-0.8 0.8C4.5 7.6 2.4 5.5 2.2 3.3z" fill="#fff"/></svg>012.555.0147</li>
      <li><svg viewBox="0 0 10 10"><circle cx="5" cy="5" r="5" fill="#ee5424"/><rect x="2.3" y="3.2" width="5.4" height="3.6" fill="#fff"/><path d="M2.3 3.2L5 5.3l2.7-2.1" stroke="#ee5424" stroke-width=".7" fill="none"/></svg>info@waypointhq</li>
      <li><svg viewBox="0 0 10 10"><circle cx="5" cy="5" r="5" fill="#ee5424"/><circle cx="5" cy="5" r="3" fill="none" stroke="#fff" stroke-width=".7"/><path d="M2 5h6M5 2v6" stroke="#fff" stroke-width=".7"/></svg>www.waypointhq.com</li>
    </ul>
    <p class="address">Suite 000, JS building,<br>Cityname, country name</p>
    <div class="name-band"><span class="person">Yourname here</span></div>
    <div class="role-pill">Director</div>
  </section>

  <section class="card card-back back-plum">
    <div class="brand-name">waypoint</div>
    <div class="stripe"></div>
    <div class="stripe-accent"></div>
  </section>

  <section class="card card-back back-orange">
    <div class="brand-name">waypoint</div>
  </section>

  <section class="card card-back back-charcoal">
    <div class="brand-name">waypoint</div>
  </section>

  <span class="label" style="left:945px; top:90px;">Back 1</span>
  <span class="label" style="left:128px; top:735px;">Back 2</span>
  <span class="label" style="left:950px; top:730px;">Back 3</span>
</body>
</html>
```